Professional/modern business card design for construction company

We need a new business card design, double sided keeping it modern, sleek, professional and simple. We are an earthmoving business but do not want any pictures of machinery. I would like one side to have the logo and the other to have all the information, keeping with the colors in our logo. The business card will need to be able to be customised so we can use it for several different managers., we would also like to be able to use the design to apply it to other stationary ie. letterheads, notebooks etc. We do not really have a tag line but we could put on there that we specialise in - Agriculture, Civil Construction and Mining.

Contact Information for Business Card

Brolga Ridge Excavations Pty Ltd
ABN 58 402 937 615
82 Gumleaf Creek Road, Moree NSW 2400

Harold Benton
Managing Director
P 0418 639 204
E haroldbenton@brolgaridgeexc.com.au

Font styles to use
Serif
Sans Serif

Requirements
Nice to have
• I have attached some examples of ideas.
Should not have
• images of machinery

```html
<!DOCTYPE html>
<html lang="en">
<head>
<meta charset="utf-8">
<title>Brolga Ridge Excavations – Business Card</title>
<link href="https://fonts.googleapis.com/css2?family=Lato:wght@400;700;900&display=swap" rel="stylesheet">
<style>
  :root {
    --orange: #f58a1f;
    --charcoal: #3a3a3a;
    --text: #333333;
    --paper: #ffffff;
    --backdrop: #d9d9d9;
    --rule: rgba(255,255,255,0.75);
  }
  * { box-sizing: border-box; margin: 0; padding: 0; }
  html, body { width: 1200px; height: 900px; overflow: hidden; }
  body {
    background: var(--backdrop);
    font-family: "Lato", Arial, sans-serif;
    position: relative;
  }
  .card {
    position: absolute;
    width: 640px;
    height: 366px;
    border-radius: 30px;
    box-shadow: 0 6px 18px rgba(0,0,0,0.18);
  }
  /* Front */
  .card-front {
    left: 60px; top: 70px;
    background: var(--orange);
    color: var(--paper);
    display: flex;
    flex-direction: column;
    align-items: center;
    justify-content: center;
    text-align: center;
  }
  .brand-name {
    font-weight: 900;
    font-size: 30px;
    line-height: 1.15;
    letter-spacing: 0.5px;
    text-transform: uppercase;
  }
  .brand-name .brand-suffix { display: block; font-size: 22px; }
  .specialty {
    margin-top: 34px;
    width: 380px;
  }
  .specialty-label {
    font-size: 15px;
    letter-spacing: 1.5px;
    text-transform: uppercase;
    padding-bottom: 6px;
    border-bottom: 1px dotted var(--rule);
  }
  .specialty-list {
    font-size: 17px;
    padding-top: 6px;
  }
  /* Back */
  .card-back {
    left: 500px; top: 470px;
    background: var(--paper);
    color: var(--text);
  }
  .back-brand {
    position: absolute;
    left: 40px; top: 110px;
    color: var(--charcoal);
    font-weight: 900;
    font-size: 22px;
    line-height: 1.15;
    text-transform: uppercase;
  }
  .company-info {
    position: absolute;
    right: 40px; top: 40px;
    text-align: right;
    font-size: 16px;
    line-height: 1.35;
  }
  .company-info .accent { color: var(--orange); font-weight: 700; }
  .company-info .abn { margin-bottom: 22px; }
  .person {
    position: absolute;
    left: 40px; top: 200px;
  }
  .person-name {
    color: var(--orange);
    font-weight: 700;
    font-size: 21px;
    text-transform: uppercase;
    letter-spacing: 0.5px;
  }
  .person-title { font-size: 17px; margin-bottom: 14px; }
  .contact-list { list-style: none; font-size: 16px; line-height: 1.45; }
  .contact-list li { display: flex; align-items: center; gap: 8px; }
  .contact-icon { width: 14px; height: 14px; fill: var(--orange); flex: none; }
</style>
</head>
<body>

<section class="card card-front" aria-label="Business card front">
  <h1 class="brand-name">Brolga Ridge Excavations<span class="brand-suffix">Pty Ltd</span></h1>
  <div class="specialty">
    <p class="specialty-label">We specialise in</p>
    <p class="specialty-list">Agriculture, Civil Construction and Mining.</p>
  </div>
</section>

<section class="card card-back" aria-label="Business card back">
  <div class="back-brand">Brolga Ridge<br>Excavations Pty Ltd</div>

  <div class="company-info">
    <p class="abn"><span class="accent">ABN</span> 58 402 937 615</p>
    <p class="accent">Brolga Ridge Excavations Pty Ltd</p>
    <p>82 Gumleaf Creek Road</p>
    <p>Moree NSW 2400</p>
  </div>

  <div class="person">
    <p class="person-name">Harold Benton</p>
    <p class="person-title">Managing Director</p>
    <ul class="contact-list">
      <li>
        <svg class="contact-icon" viewBox="0 0 16 16" aria-hidden="true"><path d="M2 5c0-2 2-3 6-3s6 1 6 3v1h-3.5V5h-5v1H2z M4 7h8l2 7H2z"/></svg>
        0418 639 204
      </li>
      <li>
        <svg class="contact-icon" viewBox="0 0 16 16" aria-hidden="true"><path d="M1 3h14v10H1z" /><path d="M1 3l7 6 7-6" fill="none" stroke="#fff" stroke-width="1.5"/></svg>
        haroldbenton@brolgaridgeexc.com.au
      </li>
      <li>
        <svg class="contact-icon" viewBox="0 0 16 16" aria-hidden="true"><circle cx="8" cy="8" r="7"/><path d="M1 8h14M8 1c-3 3-3 11 0 14M8 1c3 3 3 11 0 14" fill="none" stroke="#fff" stroke-width="1"/></svg>
        www.brolgaridgeexc.com.au
      </li>
    </ul>
  </div>
</section>

</body>
</html>
```